BLIP! Card

The single side "business card" will be utilized to write down product information for our customers. The card needs to include our logo in josefin font and read BLIP! on the front. Our brand colors are espresso brown and copper. The back needs to be white (blank) to allow us to write information down. We want modern, bold, clean and fun.
I have attached a copy of our logo but you do not have to utilize exactly as shown.

Industry/Entity Type

Business

```html
<!DOCTYPE html>
<html lang="en">
<head>
<meta charset="utf-8">
<title>Blip! Card</title>
<link rel="stylesheet" href="https://fonts.googleapis.com/css2?family=Josefin+Sans:wght@300;400&display=swap">
<style>
  :root {
    --backdrop: #e6e4e8;
    --card-white: #ffffff;
    --espresso: #2f1f18;
    --ink: #2a1d17;
    --band-text: #ddd6d0;
  }
  * { margin: 0; padding: 0; box-sizing: border-box; }
  html, body {
    width: 1200px;
    height: 900px;
    overflow: hidden;
    background: var(--backdrop);
  }
  .canvas {
    position: relative;
    width: 1200px;
    height: 900px;
    display: flex;
    align-items: center;
    justify-content: center;
  }
  .card {
    position: relative;
    width: 440px;
    height: 770px;
    background: var(--card-white);
    box-shadow: 0 6px 18px rgba(40, 30, 40, 0.18);
    font-family: "Josefin Sans", sans-serif;
    color: var(--ink);
  }
  .brand {
    position: absolute;
    right: 36px;
    top: 415px;
    text-align: right;
  }
  .brand-name {
    font-weight: 300;
    font-size: 64px;
    line-height: 1;
    letter-spacing: 2px;
  }
  .brand-tagline {
    margin-top: 10px;
    font-weight: 300;
    font-size: 22px;
    letter-spacing: 0.3px;
  }
  .band {
    position: absolute;
    left: 0;
    right: 0;
    bottom: 0;
    height: 94px;
    background: var(--espresso);
  }
  .band-word {
    position: absolute;
    right: 22px;
    bottom: 22px;
    font-weight: 400;
    font-size: 40px;
    line-height: 1;
    color: var(--band-text);
    letter-spacing: 6px;
  }
</style>
</head>
<body>
  <main class="canvas">
    <article class="card">
      <div class="brand">
        <p class="brand-name">marlowe</p>
        <p class="brand-tagline">Jewelry &amp; Design Studio</p>
      </div>
      <div class="band">
        <p class="band-word">BLIP!</p>
      </div>
    </article>
  </main>
</body>
</html>
```